Business Card Design

About Us
VaultNet is a young and innovative company focusing on security and hosting solutions for global enterprise. To supply the high-performance, highly interconnected and low latency DDoS protection service, we distributed a large number of huge scrubbing centers all over the world. So VaultNet is the first choice for enterprise to protect their network security.

Task detail
1. We hope that the business card can be filled with creativity, simple and technologe, the business card background is white, the business card text color and other colors are black, blue, green or your needs.

2. We need the source files provided by the successful bidder, such as *.psd, *.ai, etc.

3. One side contains the following:
-Logo
-Marco Sales Manager
-VAULTNET TECHNOLOGY CO., LIMITED
-Add:
9/F., Harbourgate Tower,
318 Pelton Avenue, Tsimwell, Kowloon,
HK
-Tel: 86-755-4719 2058
-Phone: 86-189 6140 3527
-Email: marco@vault-netz.example
-Web: www.vault-netz.example

4. The other side contains the following:
-Logo

5. Please find the attachment contains the logo PSD source files.

```html
<!DOCTYPE html>
<html lang="en">
<head>
<meta charset="utf-8">
<title>VaultNet Business Card</title>
<link href="https://fonts.googleapis.com/css2?family=Source+Sans+3:wght@400;600;700&display=swap" rel="stylesheet">
<style>
  :root {
    --backdrop: #e9e9e9;
    --card: #ffffff;
    --ink: #2b2b2b;
    --teal: #1fa9c6;
    --green: #6cbd45;
    --map: #ececec;
    --rule: #333333;
  }
  * { margin: 0; padding: 0; box-sizing: border-box; }
  html, body { width: 1200px; height: 1000px; overflow: hidden; }
  body {
    background: var(--backdrop);
    font-family: "Source Sans 3", Arial, sans-serif;
    color: var(--ink);
    position: relative;
  }
  .card {
    position: absolute;
    left: 265px;
    width: 665px;
    height: 397px;
    background: var(--card);
    box-shadow: 0 2px 8px rgba(0,0,0,0.18);
    overflow: hidden;
  }
  .card--front { top: 73px; }
  .card--back { top: 533px; }
  .world-map {
    position: absolute;
    background: radial-gradient(ellipse at center, var(--map) 0%, rgba(236,236,236,0.6) 60%, rgba(255,255,255,0) 100%);
  }
  .card--front .world-map { left: 240px; top: 0; width: 425px; height: 300px; }
  .card--back .world-map { left: 20px; top: 40px; width: 620px; height: 340px; }
  .brand {
    position: absolute;
    display: flex;
    align-items: center;
    gap: 10px;
    font-weight: 700;
    color: var(--green);
    line-height: 1;
  }
  .brand__mark { background: var(--teal); display: block; }
  .card--front .brand { left: 33px; top: 40px; font-size: 46px; }
  .card--front .brand__mark { width: 34px; height: 34px; }
  .card--back .brand { left: 0; right: 0; justify-content: center; top: 160px; font-size: 70px; }
  .card--back .brand__mark { width: 52px; height: 52px; }
  .person { position: absolute; left: 33px; top: 212px; }
  .person__name { color: var(--teal); font-weight: 700; font-size: 21px; line-height: 1.05; }
  .person__title { font-size: 17px; line-height: 1.2; }
  .divider { position: absolute; left: 0; right: 0; top: 266px; height: 2px; background: var(--rule); }
  .contacts { position: absolute; left: 33px; top: 282px; list-style: none; }
  .contacts li { display: flex; align-items: center; gap: 7px; font-size: 15.5px; height: 22px; }
  .contacts svg { width: 14px; height: 14px; fill: var(--teal); flex: none; }
  .company { position: absolute; right: 32px; top: 282px; text-align: right; }
  .company__name { font-weight: 700; font-size: 16.5px; line-height: 22px; letter-spacing: 0.2px; }
  .company__address { font-size: 15.5px; line-height: 22px; }
</style>
</head>
<body>
  <section class="card card--front">
    <div class="world-map" role="img" aria-label="Faint grey world map in the background"></div>
    <div class="brand"><span class="brand__mark"></span>VaultNet</div>
    <div class="person">
      <p class="person__name">Marco</p>
      <p class="person__title">Sales Manager</p>
    </div>
    <div class="divider"></div>
    <ul class="contacts">
      <li><svg viewBox="0 0 14 14"><path d="M4 0h6a1 1 0 0 1 1 1v12a1 1 0 0 1-1 1H4a1 1 0 0 1-1-1V1a1 1 0 0 1 1-1zm0.5 1.5v10h5v-10z"/></svg>86-755-4719 2058</li>
      <li><svg viewBox="0 0 14 14"><path d="M1 4c0-2 3-3 6-3s6 1 6 3v1H10V3.5H4V5H1zM3 6h8l2 7H1z"/></svg>86-189 6140 3527</li>
      <li><svg viewBox="0 0 14 14"><path d="M0 3h14v8H0zm1 1l6 4 6-4v-.2H1z"/></svg>marco@vault-netz.example</li>
      <li><svg viewBox="0 0 14 14"><circle cx="7" cy="7" r="6.5"/><path d="M0.5 7h13M7 0.5v13" stroke="#fff" stroke-width="1"/></svg>www.vault-netz.example</li>
    </ul>
    <div class="company">
      <p class="company__name">VAULTNET TECHNOLOGY CO., LIMITED</p>
      <p class="company__address">9/F., Harbourgate Tower,<br>318 Pelton Avenue, Tsimwell, Kowloon,<br>HK</p>
    </div>
  </section>

  <section class="card card--back">
    <div class="world-map" role="img" aria-label="Faint grey world map behind the logo"></div>
    <div class="brand"><span class="brand__mark"></span>VaultNet</div>
  </section>
</body>
</html>
```